Lorvane Cabinets Quality Custom Built Kitchens, Vanity Units, Robes ect

Hi,
Was after a new design for our business cards,
we are a cabinet making business and pride ourselves in quality custom built Kitchens, Vanity units, robes ect.
we have been around for over 20 years and we are trying to modernize our card logo.
Looking for something eye catching, bold and exciting
family ran and operated business, we work with builders and also have a large private clientel.

Thanks

Industry/Entity Type

Business

Contact Information for Business Card

Lorvane Cabinets

Font styles to use
Serif
Script

Requirements
Must have
• Priscilla 0471836259 lvcabinets@marrowbay.net
• Po Box 2786
• 5C Halloway Court Dunmorrow Vic 3911
• Phone (03)58291467 Fax (03) 58296014
Nice to have
• Quality Custom Built Kitchens & Vanity Units

```html
<!DOCTYPE html>
<html lang="en">
<head>
<meta charset="utf-8">
<title>Lorvane Cabinets – Business Card</title>
<link rel="stylesheet" href="https://fonts.googleapis.com/css2?family=Arvo:wght@400;700&family=Noto+Serif:ital,wght@0,400;0,700;1,400&display=swap">
<style>
  :root {
    --stage: #ece8e3;
    --wine: #7e1418;
    --wine-deep: #5e0d10;
    --wine-light: #9a2a2e;
    --paper: #ffffff;
    --paper-shade: #ececec;
    --ink: #3a3a3a;
    --ink-soft: #4a4a4a;
    --accent: #e07a2a;
  }
  * { box-sizing: border-box; margin: 0; padding: 0; }
  html, body {
    width: 1200px; height: 1023px; overflow: hidden;
    background: var(--stage);
  }
  .stage {
    width: 1200px; height: 1023px;
    display: flex; flex-direction: column;
    align-items: center; justify-content: center; gap: 40px;
  }
  .card {
    width: 820px; height: 469px;
    position: relative;
    box-shadow: 0 6px 18px rgba(0,0,0,0.18);
  }

  /* Front */
  .card-front {
    background: var(--wine);
    padding: 12px;
  }
  .card-front .mat {
    width: 100%; height: 100%;
    background: var(--paper);
    padding: 10px;
  }
  .card-front .frame {
    width: 100%; height: 100%;
    border: 7px solid var(--wine);
    background: radial-gradient(ellipse at 50% 40%, var(--paper) 55%, var(--paper-shade) 100%);
    position: relative;
    font-family: "Noto Serif", Georgia, serif;
    color: var(--ink-soft);
  }
  .front-title {
    position: absolute; left: 60px; top: 46px;
    font-family: "Arvo", Georgia, serif; font-weight: 700;
    font-size: 50px; color: var(--ink); letter-spacing: 0.5px;
  }
  .contact {
    position: absolute; left: 0; right: 0; top: 150px;
    text-align: center; font-size: 17px; line-height: 1.6;
  }
  .contact .person {
    font-family: "Arvo", Georgia, serif; font-weight: 700;
    color: var(--wine); font-size: 21px;
  }
  .contact .label { color: var(--accent); }
  .contact .bracket { color: var(--ink-soft); }
  .contact .gap { height: 18px; }
  .address {
    position: absolute; left: 60px; bottom: 40px;
    font-size: 17px;
  }

  /* Back */
  .card-back {
    background: linear-gradient(125deg, var(--wine-light) 0%, var(--wine) 45%, var(--wine-deep) 100%);
    display: flex; flex-direction: column; align-items: center; justify-content: center;
    color: var(--paper);
  }
  .back-title {
    font-family: "Arvo", Georgia, serif; font-weight: 700;
    font-size: 60px; letter-spacing: 1px;
  }
  .tagline {
    font-family: "Noto Serif", Georgia, serif; font-style: italic;
    font-size: 22px; margin-top: 8px;
  }
</style>
</head>
<body>
<main class="stage">
  <section class="card card-front">
    <div class="mat">
      <div class="frame">
        <h1 class="front-title">Lorvane Cabinets</h1>
        <div class="contact">
          <p class="person">Priscilla</p>
          <p>Mob: 04 7183 6259</p>
          <div class="gap"></div>
          <p><span class="bracket">[</span><span class="label">P</span><span class="bracket">]</span>: 03 5829 1467</p>
          <p><span class="bracket">[</span><span class="label">F</span><span class="bracket">]</span>: 03 5829 6014</p>
          <div class="gap"></div>
          <p><span class="bracket">[</span><span class="label">E</span><span class="bracket">]</span>: lvcabinets@marrowbay.net</p>
        </div>
        <p class="address">Po Box 2786, 5C Halloway Court Dunmorrow Vic 3911</p>
      </div>
    </div>
  </section>

  <section class="card card-back">
    <h2 class="back-title">Lorvane Cabinets</h2>
    <p class="tagline">Quality Custom Built Kitchens &amp; Vanity Units</p>
  </section>
</main>
</body>
</html>
```